MARBLED SPARROW WEB DESIGN PROJECT

We are a brand new company called "Marbled Sparrow" which specialise in one-off Vintage Clothing. We would like somebody to design a web page which will be the sole income for our company. Our main aim is to have an easy searchable website which is user friendly. The key to the website is to target people who do not like the idea of op-shopping but love vintage clothes - this website will be the answer.
Updates

This website will need to be coded to work with Tin Lantern - Please read this before you start. https://help.tinlantern.example/articles/Public/How-do-I-create-custom-template-files-for-my-store

Hi everyone, Just want to make note that the this website is for young people. Just so people a clear I want modern young people dressed in Vintage clothes as this is that reality and what they would like to see. Not people dressed like they are going to a fancy dress party, i.e. dresses like it was that era. Thanks Mirela

Coding

Coded - Design and coding required

```html
<!DOCTYPE html>
<html lang="en">
<head>
<meta charset="utf-8">
<title>Marbled Sparrow — Unique Vintage Fashion and Accessories</title>
<link href="https://fonts.googleapis.com/css2?family=Raleway:wght@400;500;600;700;800&family=Oswald:wght@300;700&family=Playfair+Display:ital@1&display=swap" rel="stylesheet">
<style>
:root{
  --pink:#e8336d;
  --ink:#222;
  --muted:#777;
  --line:#ddd;
  --soft:#f2f2f2;
  --footer:#2b2b2b;
  --footer-deep:#1d1d1d;
  --footer-muted:#aaa;
  --white:#fff;
}
*{box-sizing:border-box;margin:0;padding:0}
html,body{width:762px;height:1200px;overflow:hidden;background:var(--white)}
body{position:relative;font-family:"Raleway",sans-serif;color:var(--ink);font-size:8px}
.abs{position:absolute}
a{color:inherit;text-decoration:none}

/* header */
.brand{left:70px;top:16px}
.brand-name{font-size:22px;font-weight:700;color:var(--pink);letter-spacing:.5px}
.brand-tag{font-size:7.5px;font-weight:500;margin-top:6px;color:#333}
.toplinks{right:70px;top:10px;font-size:8px;color:var(--muted)}
.search{left:295px;top:30px;width:168px;height:19px;border:1px solid var(--pink);color:var(--pink);font-size:7px;padding:5px 7px}
.search svg{position:absolute;right:6px;top:4px}
.chip{top:30px;height:19px;border:1px solid var(--line);font-size:7px;color:var(--muted);display:flex;align-items:center;gap:6px;padding:0 6px}
.flag{width:10px;height:7px;background:#c8cde0;border:1px solid #b33}
.account-links{right:70px;top:59px;font-size:8px;color:var(--muted);display:flex;gap:14px}
.account-links span::before{content:"";display:inline-block;width:6px;height:6px;background:#999;margin-right:6px}

/* nav */
.nav{left:70px;top:89px;width:622px;height:28px;background:var(--ink);display:flex;align-items:center;font-size:8.5px;color:var(--white);font-weight:500}
.nav a{padding:0 23px;height:28px;line-height:28px}
.nav .active{background:var(--pink);width:58px;text-align:center;padding:0}
.nav .ship{margin-left:auto;background:var(--pink);font-size:6.5px;font-weight:700;padding:0 10px;width:145px;text-align:center}

/* hero */
.hero{left:70px;top:117px;width:622px;height:274px;background:linear-gradient(100deg,#e9b78d 0%,#f3d2b0 35%,#c9a384 60%,#8f8a5a 85%,#6f7a4a 100%)}
.hero-copy{left:102px;top:152px;width:216px;text-align:center}
.hero-script{font-family:"Playfair Display",serif;font-style:italic;color:var(--pink);font-size:18px;display:flex;align-items:center;gap:6px;justify-content:center}
.hero-script::before,.hero-script::after{content:"";width:48px;height:1px;background:var(--pink)}
.hero-title{font-family:"Oswald",sans-serif;font-weight:700;font-size:50px;line-height:46px;color:#333;letter-spacing:-1px}
.hero-rule{height:3px;background:var(--pink);margin:6px 0 6px}
.hero-sub{font-family:"Oswald",sans-serif;font-weight:300;color:var(--pink);font-size:21px}
.shop-now{left:160px;top:320px;width:99px;height:34px;background:var(--pink);color:var(--white);font-size:10px;display:flex;align-items:center;justify-content:center;gap:10px;box-shadow:2px 2px 0 #b51f50}

/* promo tiles */
.tile{top:397px;width:203px;height:110px;color:var(--white)}
.tile-title{font-weight:800;font-size:18px}
.btn-outline{border:1px solid var(--white);font-size:8.5px;font-weight:600;padding:4px 13px;display:inline-block}

/* featured */
.soft{left:0;top:507px;width:762px;height:325px;background:linear-gradient(180deg,var(--white),var(--soft) 40px)}
.section-title{left:70px;top:538px;font-size:14px;font-weight:600}
.section-rule{left:70px;top:563px;width:624px;height:2px;background:var(--line)}
.section-rule::before{content:"";position:absolute;left:0;top:0;width:179px;height:2px;background:var(--pink)}
.arrowbtn{top:538px;width:15px;height:15px;border-radius:50%;background:#ddd}
.product{top:579px;width:144px}
.photo{height:182px}
.price-row{display:flex;justify-content:space-between;margin-top:10px;padding:0 2px}
.price{color:var(--pink);font-weight:700;font-size:10px}
.stars{color:#ccc;font-size:9px;letter-spacing:3px}
.pname{margin-top:8px;padding:0 2px;font-size:10.5px;font-weight:500;color:#666}

/* testimonial */
.review-photo{left:95px;top:854px;width:88px;height:99px;background:#ddd;padding:6px}
.review-photo div{width:100%;height:100%;background:linear-gradient(160deg,#9b7b88,#c44a66 60%,#5a4660)}
.reviewer{left:198px;top:859px;font-size:13.5px;font-weight:600;display:flex;align-items:center;gap:22px}
.reviewer .stars{color:var(--pink);font-size:11px;letter-spacing:3px}
.review-text{left:198px;top:884px;width:470px;font-size:7.8px;line-height:15.5px;color:#555}
.review-link{left:198px;top:940px;font-size:8px;font-weight:600;color:var(--pink)}
.chev{top:888px}

/* footer */
.footer{left:0;top:978px;width:762px;height:184px;background:var(--footer)}
.fcol{top:1000px;color:var(--white)}
.fcol h4{font-size:11.5px;font-weight:600;margin-bottom:17px}
.fcol li{list-style:none;font-size:8.5px;line-height:15.2px}
.contact-line{font-family:Georgia,serif;font-size:8px;color:var(--footer-muted);display:flex;align-items:center;gap:12px}
.social{top:1082px;width:24px;height:24px;border:1.5px solid var(--white);border-radius:50%}
.signup{left:507px;top:1122px;width:161px;height:17px;display:flex;font-size:7px}
.signup .field{flex:1;background:#ddd;color:#333;padding:4px 11px;font-weight:500}
.signup .submit{background:var(--pink);color:var(--white);width:41px;text-align:center;padding-top:4px;font-weight:600}
.bottom{left:0;top:1162px;width:762px;height:38px;background:var(--footer-deep);color:var(--white);font-size:8px;display:flex;align-items:center;justify-content:space-between;padding:0 70px}
</style>
</head>
<body>

<header>
  <div class="abs brand">
    <div class="brand-name">Marbled Sparrow</div>
    <div class="brand-tag">Unique Vintage Fashion and Accessories</div>
  </div>
  <div class="abs toplinks">Login &nbsp;|&nbsp; Sign In &nbsp;|&nbsp; My Account</div>
  <div class="abs search">Search one of vintage items
    <svg width="9" height="9" viewBox="0 0 10 10"><circle cx="4" cy="4" r="3" fill="none" stroke="#e8336d" stroke-width="1.3"/><line x1="6.3" y1="6.3" x2="9" y2="9" stroke="#e8336d" stroke-width="1.3"/></svg>
  </div>
  <div class="abs chip" style="left:469px;width:63px"><span class="flag"></span>English</div>
  <div class="abs chip" style="left:538px;width:68px">$ &nbsp;US DOLOR</div>
  <div class="abs chip" style="left:611px;width:82px">
    <svg width="9" height="8" viewBox="0 0 10 9"><path d="M0 1h2l1.5 5h5L10 2H3" fill="none" stroke="#888" stroke-width="1.2"/></svg>Cart : (empty)</div>
  <div class="abs account-links"><span>My Wish list (0)</span><span>My Account</span><span>View Cart</span><span>Checkout</span></div>
</header>

<nav class="abs nav">
  <a class="active">HOME</a><a>MAN</a><a>WOMEN</a><a>STYLE TIPS</a><a>FAQS</a><a>CONTACT US</a>
  <a class="ship">FREE SHIPING ON ORDER OVER $100</a>
</nav>

<section>
  <div class="abs hero" role="img" aria-label="Young woman in a headscarf and sunglasses sitting outdoors in warm winter sunlight"></div>
  <div class="abs hero-copy">
    <div class="hero-script">Crazy</div>
    <div class="hero-title">CRAZY<br>WINTER</div>
    <div class="hero-rule"></div>
    <div class="hero-sub">WOMAN COLLECTION</div>
  </div>
  <a class="abs shop-now">SHOP NOW <span>▸</span></a>
</section>

<div class="abs soft"></div>

<section>
  <div class="abs tile" role="img" aria-label="Woman in dark sunglasses and a black coat" style="left:70px;background:linear-gradient(90deg,#8a8a8a,#5c5c5c 60%,#333)"></div>
  <div class="abs" style="left:90px;top:412px;color:#fff">
    <div class="tile-title">STYLE TIPS</div>
    <div style="font-size:8.5px;line-height:13px;margin:5px 0 10px">Orders over $100will<br>receive FREE shipping!</div>
    <span class="btn-outline" style="padding:5px 14px">Subscribe</span>
  </div>
  <div class="abs tile" role="img" aria-label="Young man in a vintage jacket and tie by a stone building" style="left:280px;background:linear-gradient(90deg,#6e6e6a,#8e8a84 50%,#4c4c4c)"></div>
  <div class="abs" style="left:280px;top:442px;width:203px;text-align:center;color:#fff">
    <div class="tile-title">SHOP ERA</div>
    <span class="btn-outline" style="margin-top:3px">Subscribe</span>
  </div>
  <div class="abs tile" role="img" aria-label="Woman in sunglasses with hands raised to her head" style="left:490px;background:linear-gradient(180deg,#6b6b70,#9a9598 55%,#d64f7a 70%,#e8336d)"></div>
  <div class="abs" style="left:498px;top:480px;display:flex;align-items:center;gap:6px;color:#fff">
    <span style="font-weight:700;font-size:12.5px">JOIN OUR VIP CLUB</span>
    <span class="btn-outline">Subscribe</span>
  </div>
</section>

<section>
  <h2 class="abs section-title">FEATURED PRODUCTS</h2>
  <div class="abs section-rule"></div>
  <div class="abs arrowbtn" style="left:655px"></div>
  <div class="abs arrowbtn" style="left:677px"></div>

  <div class="abs product" style="left:70px">
    <div class="photo" role="img" aria-label="Woman in a black hat and dark party dress holding a shopping bag" style="background:linear-gradient(160deg,#cfd0d6,#7d7f8c 50%,#2d3040)"></div>
    <div class="price-row"><span class="price">ONLY $25</span><span class="stars">★★★★★</span></div>
    <div class="pname">PARTY DRESS</div>
  </div>
  <div class="abs product" style="left:230px">
    <div class="photo" role="img" aria-label="Woman in a red double breasted coat on a city street" style="background:linear-gradient(90deg,#8a8e96,#c9272d 45%,#b01c24 60%,#6d7380)"></div>
    <div class="price-row"><span class="price">ONLY $25</span><span class="stars">★★★★★</span></div>
    <div class="pname">DOUBLE BREASTED COAT</div>
  </div>
  <div class="abs product" style="left:389px">
    <div class="photo" role="img" aria-label="Woman in a floral hippy dress in a grass field" style="background:linear-gradient(180deg,#6fa1c9,#a9c4d6 45%,#c48f6a 65%,#7d7a3e)"></div>
    <div class="price-row"><span class="price">ONLY $25</span><span class="stars">★★★★★</span></div>
    <div class="pname">HIPPY DRESS</div>
  </div>
  <div class="abs product" style="left:547px">
    <div class="photo" role="img" aria-label="Man walking a runway in a dark suit and high pants" style="background:linear-gradient(90deg,#1a1c22,#3a3f4a 50%,#16181c)"></div>
    <div class="price-row"><span class="price">ONLY $25</span><span class="stars">★★★★★</span></div>
    <div class="pname">HIGH PANT</div>
  </div>
</section>

<section>
  <svg class="abs chev" style="left:70px" width="10" height="16" viewBox="0 0 10 16"><path d="M8 1L2 8l6 7" fill="none" stroke="#666" stroke-width="2"/></svg>
  <svg class="abs chev" style="left:682px" width="10" height="16" viewBox="0 0 10 16"><path d="M2 1l6 7-6 7" fill="none" stroke="#666" stroke-width="2"/></svg>
  <div class="abs review-photo"><div role="img" aria-label="Smiling customer holding shopping bags"></div></div>
  <div class="abs reviewer">Talia Brenner <span class="stars">★★★★★</span></div>
  <p class="abs review-text">Lorem ipsum dolor sit amet, consectetur adipiscing elit. Pellentesque quis condimentum sapien. Ut pretium euismod velit, eget dapibus erat tincidunt id. Sed at magna varius, euismod libero sit amet, euismod lectus. In hac habitasse platea dictumst. Quisque viverra tempor feugiat.</p>
  <a class="abs review-link">Lorem Ipsum</a>
</section>

<footer>
  <div class="abs footer"></div>
  <div class="abs fcol" style="left:70px"><h4>Marbled Sparrow</h4><ul><li>About us</li><li>Terms of use</li><li>Privacy policy</li><li>Press</li></ul></div>
  <div class="abs fcol" style="left:196px"><h4>Contact with us</h4><ul><li>Contact Us</li><li>My Account</li><li>Style Tips</li><li>FAQs</li><li>Shipping</li><li>Track your order</li><li>Size chart</li></ul></div>
  <div class="abs fcol" style="left:321px"><h4>Shop By Popular Categories</h4><ul><li>Man</li><li>Woman</li><li>Accessories</li><li>Bags</li><li>Shoes</li></ul></div>
  <div class="abs fcol" style="left:506px">
    <h4 style="font-size:10.5px;margin-top:2px">CONTACT US</h4>
    <div class="contact-line">
      <svg width="20" height="12" viewBox="0 0 20 12"><rect x="5" y="1" width="14" height="10" fill="#fff"/><path d="M5 1l7 6 7-6" fill="none" stroke="#2b2b2b"/><line x1="0" y1="4" x2="4" y2="4" stroke="#fff"/><line x1="1" y1="7" x2="4" y2="7" stroke="#fff"/></svg>
      SALES@MARBLEDSPARROW.EXAMPLE</div>
    <div class="contact-line" style="margin-top:12px">
      <svg width="16" height="14" viewBox="0 0 16 14"><path d="M3 1c-2 1-2 4 0 7s5 5 7 5l1.5-2-3-2-1.3 1C6 9 5 8 4.5 6.5L5.6 5 4 1.5z" fill="#fff"/></svg>
      555-010-2346</div>
  </div>
  <div class="abs social" style="left:507px"></div>
  <div class="abs social" style="left:538px"></div>
  <div class="abs social" style="left:570px"></div>
  <div class="abs signup"><span class="field">Sign up for Email &amp; updates</span><span class="submit">Submit</span></div>
  <div class="abs bottom"><span>© Marbled Sparrow. All Prices are in USD.</span><span>Term &amp; Conditions &nbsp; | &nbsp; Privacy Policy</span></div>
</footer>

</body>
</html>
```